Ridgeway Fluidworks needs a website describing the repair business we are in.

Ridgeway Fluidworks is a full hydraulic repair facility. We have 2 shops. We repair and service all hydraulic cylinders, pneumatic cylinders, hydraulic pumps, motors, valves and gearboxes. Our services range from large industrial plants to the individual that owns one piece of equipment. We also offer removal and install of cylinders. Along with free pick up and delivery, within a certain distance which is usually 100 miles from one of our shops.

With over 30 years experience in the hydraulic business, we can repair or replace any job. There is not a job too big or too small, we service them all.

We have customers that send whole pieces of equipment to us to do complete overhauls on all the hydraulics. Ranging from a country club green roller to a 10 ton boom truck.

Target Market(s)

Industrial plants, road builders, dirt work companies, general contractors, owners of industrial equipment (bulldozers, excavators, loaders, scrapers, motor graders, etc.

Industry/Entity Type

Hydraulic

Number of Pages Required

5+ page

Font styles to use
Sans Serif

Colors
ec1f27
ffffff
aaaaaa

Requirements
Must have
• Information about what we offer and pictures of jobs completed.
Nice to have
• Nice stock photos of jobsites and industrial plants.
Should not have
• Any sort of comical characters.

```html
<!DOCTYPE html>
<html lang="en">
<head>
<meta charset="utf-8">
<title>Ridgeway Fluidworks — Hydraulic Repair</title>
<link href="https://fonts.googleapis.com/css2?family=Open+Sans:wght@400;600;700;800&display=swap" rel="stylesheet">
<style>
:root{
  --red:#ec1f27;
  --white:#ffffff;
  --grey:#aaaaaa;
  --ink:#222222;
  --text:#555555;
  --light:#f3f3f3;
  --dark:#1c1c1c;
}
*{box-sizing:border-box;margin:0;padding:0}
html,body{width:1200px;height:3527px;overflow:hidden}
body{font-family:"Open Sans",Arial,sans-serif;color:var(--text);background:var(--white);position:relative}
a{color:inherit;text-decoration:none}
.abs{position:absolute}
.btn{position:absolute;display:flex;align-items:center;justify-content:center;font-size:12px;font-weight:700;text-transform:uppercase;letter-spacing:.5px;color:var(--white);border-radius:3px}
.btn-red{background:var(--red)}
.btn-grey{background:var(--grey)}
.red-rule{position:absolute;width:50px;height:3px;background:var(--red)}

/* header */
.site-header{position:absolute;left:0;top:0;width:1200px;height:108px;background:var(--white)}
.brand{position:absolute;left:118px;top:20px;display:flex;align-items:center;gap:8px}
.brand-dot{width:22px;height:22px;border-radius:50%;background:var(--red)}
.brand-name{font-size:15px;font-weight:800;color:var(--red);text-transform:uppercase;line-height:1.1;width:110px}
.topbar{position:absolute;right:116px;top:18px;display:flex;gap:36px;font-size:13px;color:#444}
.topbar span{display:flex;align-items:center;gap:6px}
.topbar b{color:var(--red);font-weight:600}
.main-nav{position:absolute;left:293px;top:63px;display:flex;gap:22px;font-size:14px;font-weight:600;color:#222;text-transform:uppercase}
.main-nav a.active{color:var(--ink)}

/* hero */
.hero{position:absolute;left:0;top:108px;width:1200px;height:508px;background:linear-gradient(180deg,#8a8f93 0%,#5c5f5f 45%,#3b3a36 100%)}
.hero-shade{position:absolute;inset:0;background:rgba(0,0,0,.25)}
.hero-kicker{position:absolute;top:136px;width:100%;text-align:center;color:var(--white);font-size:15px}
.hero-title{position:absolute;top:188px;width:100%;text-align:center;color:var(--white);font-size:42px;font-weight:600;line-height:48px;text-transform:uppercase}

/* about */
.about-photo{position:absolute;left:118px;top:715px;width:374px;height:306px;background:linear-gradient(135deg,#e8e4e2,#b63a3a 55%,#5d7ea8)}
.about-body{position:absolute;left:607px;top:715px;width:480px}
.section-title{font-size:27px;font-weight:700;color:var(--ink);text-transform:uppercase}
.about-body p{margin-top:16px;font-size:14.5px;line-height:23.5px}
.features{position:absolute;top:1120px;left:0;width:1200px}
.feature{position:absolute;width:180px;text-align:center;font-size:14px;color:#333;line-height:20px}
.feature svg{display:block;margin:0 auto 10px}

/* services */
.service{position:absolute;top:1290px;width:600px;height:508px;color:var(--white);text-align:center}
.service-bg{position:absolute;inset:0}
.service-content{position:absolute;left:110px;right:110px;top:100px}
.service h3{font-size:31px;font-weight:600;margin-top:20px}
.service p{font-size:14.5px;line-height:23px;margin-top:10px}

/* gallery */
.gallery-tile{position:absolute;top:1979px;height:306px}
.arrow-disc{position:absolute;width:38px;height:38px;border-radius:50%;background:rgba(255,255,255,.75);display:flex;align-items:center;justify-content:center}

/* testimonials */
.testimonials{position:absolute;left:0;top:2466px;width:1200px;height:440px;background:linear-gradient(180deg,#4a4a4a,#2c2c2c 60%,#3a3a3a)}
.testimonials h2{position:absolute;top:90px;width:100%;text-align:center;color:var(--white);font-size:27px;font-weight:600;text-transform:uppercase}
.stars{position:absolute;top:162px;width:100%;display:flex;justify-content:center;gap:6px}
.quote{position:absolute;left:270px;width:660px;top:206px;text-align:center;color:var(--white);font-size:16px;line-height:25px}
.quote-name{position:absolute;top:306px;width:100%;text-align:center;color:var(--white);font-size:16px;font-weight:700}
.dots{position:absolute;top:350px;width:100%;display:flex;justify-content:center;gap:8px}
.dots i{width:10px;height:10px;border-radius:50%;border:1.5px solid var(--white)}
.dots i.on{background:var(--white)}

/* contact map */
.map{position:absolute;left:0;top:2906px;width:1200px;height:426px;background:linear-gradient(135deg,#dcdde6,#c9cbd8)}
.contact-card{position:absolute;left:725px;top:3028px;width:303px;height:208px;background:rgba(255,255,255,.88);padding:24px 30px}
.contact-card h4{font-size:24px;font-weight:400;color:#333}
.contact-line{display:flex;gap:12px;font-size:14px;color:#555;line-height:21px;margin-top:12px}
.contact-line b{color:var(--red);font-weight:400}
.contact-line u{color:var(--red)}

/* footer */
.site-footer{position:absolute;left:0;top:3332px;width:1200px;height:195px;background:var(--white)}
.footer-brand{position:absolute;left:140px;top:28px;text-align:center;width:100px}
.footer-brand .brand-dot{margin:0 auto 6px}
.footer-brand span{font-size:13px;font-weight:800;color:var(--red);text-transform:uppercase;line-height:1.1}
.footer-nav{position:absolute;left:322px;top:53px;display:flex;gap:16px;font-size:13px;color:#666}
.footer-nav .active{color:var(--red)}
.social{position:absolute;left:990px;top:56px;display:flex;gap:20px}
.social i{width:14px;height:14px;border-radius:50%;background:#bbb}
.social i.on{background:var(--red)}
.footer-rule{position:absolute;left:118px;right:118px;top:136px;height:1px;background:#e2e2e2}
.copyright{position:absolute;left:118px;top:154px;font-size:11.5px;color:#777}
.legal{position:absolute;right:118px;top:154px;display:flex;gap:18px;font-size:11.5px;color:#777}
</style>
</head>
<body>

<header class="site-header">
  <div class="brand"><div class="brand-dot"></div><div class="brand-name">Ridgeway Fluidworks</div></div>
  <div class="topbar">
    <span><svg width="11" height="14" viewBox="0 0 12 16"><path d="M6 0a6 6 0 0 0-6 6c0 4.5 6 10 6 10s6-5.5 6-10a6 6 0 0 0-6-6zm0 8.5A2.5 2.5 0 1 1 6 3.5a2.5 2.5 0 0 1 0 5z" fill="#999"/></svg>1280 Larkfield Road, Brennan, MN 56012</span>
    <span><svg width="13" height="13" viewBox="0 0 16 16"><path d="M3.6 1 6 3.7 4.7 5.6a9 9 0 0 0 5.7 5.7L12.3 10 15 12.4l-1.4 2.4C7.5 15 1 8.5 1.2 2.4z" fill="#999"/></svg>Call Us: <b>555-014-2270</b></span>
  </div>
  <nav class="main-nav">
    <a class="active">Home</a><a>About Us</a><a>Our Services</a><a>Products</a><a>Testimonials</a><a>Gallery</a>
  </nav>
  <a class="btn btn-red" style="left:955px;top:56px;width:128px;height:36px">Contact Us</a>
</header>

<section class="hero" role="img" aria-label="Trailer carrying a yellow hydraulic cylinder outside the repair shop">
  <div class="hero-shade"></div>
  <div class="hero-kicker">Welcome To Ridgeway Fluidworks</div>
  <h1 class="hero-title">We Offer The Best Hydlraulics<br>Services Solutions</h1>
  <a class="btn btn-grey" style="left:428px;top:325px;width:149px;height:38px">Learn More</a>
  <a class="btn btn-red" style="left:621px;top:325px;width:149px;height:38px">Contact Us</a>
</section>

<div class="about-photo" role="img" aria-label="Technician servicing red hydraulic hoses"></div>
<div class="red-rule" style="left:607px;top:718px"></div>
<div class="about-body">
  <h2 class="section-title" style="margin-top:12px">About Us</h2>
  <p>Ridgeway Fluidworks is a full hydraulic repair facility. We have 2 shops. We repair and service all hydraulic cylinders, pneumatic cylinders, hydraulic pumps, motors, valves and gearboxes. Our services range from large industrial plants to the individual that owns one piece of equipment. We also offer removal and install of cylinders. Along with free pick up and delivery, within a certain distance which is usually 100 miles from one of our shops.</p>
</div>
<a class="btn btn-grey" style="left:607px;top:986px;width:118px;height:30px;font-size:10px">Learn More</a>
<a class="btn btn-red" style="left:755px;top:986px;width:155px;height:30px;font-size:10px">▸ Watch Our Video</a>

<div class="features">
  <div class="feature" style="left:181px"><svg width="62" height="62" viewBox="0 0 62 62" fill="none" stroke="#ec1f27" stroke-width="2.5"><rect x="10" y="24" width="42" height="30"/><rect x="6" y="16" width="50" height="10"/><path d="M31 16v38M31 16c-6-10-16-6-10 0M31 16c6-10 16-6 10 0"/></svg>Free Pick Up and<br>Delivery</div>
  <div class="feature" style="left:402px"><svg width="62" height="62" viewBox="0 0 62 62" fill="none" stroke="#ec1f27" stroke-width="2.5"><circle cx="31" cy="24" r="16"/><circle cx="31" cy="24" r="9"/><path d="M21 37l-6 18 8-4 4 7 4-14M41 37l6 18-8-4-4 7"/></svg>+30 Years of<br>Experience</div>
  <div class="feature" style="left:621px"><svg width="62" height="62" viewBox="0 0 62 62" fill="none" stroke="#ec1f27" stroke-width="2.5"><circle cx="31" cy="31" r="25"/><path d="M20 30h6v16h-6zM26 44h14c3 0 4-2 4-4l2-9c0-2-1-3-3-3h-9l1-7c0-3-4-4-5-1l-4 8"/></svg>Best Services<br>&amp; Prices</div>
  <div class="feature" style="left:847px"><svg width="62" height="62" viewBox="0 0 62 62" fill="none" stroke="#ec1f27" stroke-width="2.5"><path d="M14 12l8 9-4 5a26 26 0 0 0 16 16l5-4 9 8-5 7C24 55 7 38 7 18z"/><circle cx="42" cy="20" r="13"/><text x="42" y="24" font-size="11" font-family="Open Sans" fill="#ec1f27" stroke="none" text-anchor="middle" font-weight="700">24</text></svg>Support Avaible<br>24h/7d</div>
</div>

<section class="service" style="left:0">
  <div class="service-bg" role="img" aria-label="Industrial plant piping and valves" style="background:linear-gradient(135deg,#4b5a5c,#2f3a3b 60%,#56686a)"></div>
  <div class="service-bg" style="background:rgba(20,25,28,.45)"></div>
  <div class="service-content">
    <svg width="64" height="64" viewBox="0 0 64 64" fill="none" stroke-width="5" stroke-linecap="round"><path d="M14 50 50 14" stroke="#ec1f27"/><path d="M14 14 50 50" stroke="#ffffff"/></svg>
    <h3>Repair &amp; Service</h3>
    <p>We repair and service all hydraulic cylinders, pneumatic cylinders, hydraulic pumps, motors, valves and gearboxes. Our services range from large industrial plants to the individual that owns one piece of equipment</p>
  </div>
  <a class="btn btn-grey" style="left:237px;top:366px;width:126px;height:40px">Learn More</a>
</section>
<section class="service" style="left:600px">
  <div class="service-bg" role="img" aria-label="Teal pipework in a pumping station" style="background:linear-gradient(135deg,#3d6f74,#2a4c50 55%,#5d8a8c)"></div>
  <div class="service-bg" style="background:rgba(20,30,35,.4)"></div>
  <div class="service-content">
    <svg width="64" height="64" viewBox="0 0 64 64" fill="none" stroke="#ec1f27" stroke-width="5"><path d="M8 20h14l20 24h14M8 44h14l6-7M36 27l6-7h14M50 13l7 7-7 7M50 37l7 7-7 7"/></svg>
    <h3>Remove &amp; Install</h3>
    <p>Lorem ipsum dolor sit amet, consectetur adipiscing elit. Nullam odio dolor, congue nec lorem et, euismod commodo ante. Quisque fringilla maximus metus, ut dignissim urna. Integer tincidunt dapibus nisi rutrum.</p>
  </div>
  <a class="btn btn-red" style="left:198px;top:366px;width:148px;height:40px">Learn More</a>
</section>

<div class="red-rule" style="left:575px;top:1884px"></div>
<h2 class="section-title abs" style="top:1897px;width:1200px;text-align:center;font-size:26px">Our Gallery</h2>
<div class="gallery-tile" role="img" aria-label="Yellow repaired hydraulic cylinder" style="left:0;width:224px;background:linear-gradient(135deg,#5a4a3a,#d8b21c 50%,#7a6a55)"></div>
<div class="gallery-tile" role="img" aria-label="Blue hydraulic pump on a pallet" style="left:240px;width:353px;background:linear-gradient(135deg,#3a3d40,#8a6a45 55%,#2f5aa0)"></div>
<div class="gallery-tile" role="img" aria-label="Large rebuilt cylinders on the shop floor" style="left:609px;width:353px;background:linear-gradient(135deg,#6f6a62,#9a9a98 55%,#5a4d42)"></div>
<div class="gallery-tile" role="img" aria-label="Crate of finished cylinders" style="left:979px;width:221px;background:linear-gradient(135deg,#6d5840,#a8a8aa 50%,#6b5a48)"></div>
<div class="arrow-disc" style="left:48px;top:2113px"><svg width="10" height="14"><path d="M8 1 2 7l6 6" stroke="#555" stroke-width="2" fill="none"/></svg></div>
<div class="arrow-disc" style="left:1110px;top:2113px"><svg width="10" height="14"><path d="M2 1l6 6-6 6" stroke="#555" stroke-width="2" fill="none"/></svg></div>
<svg class="abs" style="left:767px;top:2114px" width="36" height="36" viewBox="0 0 36 36" fill="none" stroke="#fff" stroke-width="2.5"><path d="M4 12V4h8M24 4h8v8M32 24v8h-8M12 32H4v-8M4 4l9 9M32 4l-9 9M32 32l-9-9M4 32l9-9"/></svg>
<a class="btn btn-red" style="left:527px;top:2330px;width:148px;height:37px">View All</a>

<section class="testimonials" role="img" aria-label="Black and white industrial plant background">
  <h2>Our Testimonials</h2>
  <div class="stars">
    <svg width="28" height="28" viewBox="0 0 24 24"><path d="M12 2l3 6.5 7 .7-5.3 4.7 1.6 7L12 17.3 5.7 21l1.6-7L2 9.2l7-.7z" fill="#f5c518"/></svg>
    <svg width="28" height="28" viewBox="0 0 24 24"><path d="M12 2l3 6.5 7 .7-5.3 4.7 1.6 7L12 17.3 5.7 21l1.6-7L2 9.2l7-.7z" fill="#f5c518"/></svg>
    <svg width="28" height="28" viewBox="0 0 24 24"><path d="M12 2l3 6.5 7 .7-5.3 4.7 1.6 7L12 17.3 5.7 21l1.6-7L2 9.2l7-.7z" fill="#f5c518"/></svg>
    <svg width="28" height="28" viewBox="0 0 24 24"><path d="M12 2l3 6.5 7 .7-5.3 4.7 1.6 7L12 17.3 5.7 21l1.6-7L2 9.2l7-.7z" fill="#f5c518"/></svg>
    <svg width="28" height="28" viewBox="0 0 24 24"><path d="M12 2l3 6.5 7 .7-5.3 4.7 1.6 7L12 17.3 5.7 21l1.6-7L2 9.2l7-.7z" fill="#f5c518"/></svg>
  </div>
  <p class="quote">"I would also like to say thank you to all your staff. I like Ridgeway Fluidworks more and more each day because it makes my life a lot easier. It's all good. We can't understand how we've been living without you."</p>
  <div class="quote-name">– Marcus T. Hale</div>
  <div class="dots"><i class="on"></i><i></i><i></i><i></i><i></i></div>
  <svg class="abs" style="left:172px;top:142px" width="18" height="36"><path d="M16 2 2 18l14 16" stroke="#ddd" stroke-width="2" fill="none"/></svg>
  <svg class="abs" style="left:1008px;top:142px" width="18" height="36"><path d="M2 2l14 16L2 34" stroke="#ddd" stroke-width="2" fill="none"/></svg>
</section>

<section class="map" role="img" aria-label="Street map around the shop location"></section>
<div class="contact-card">
  <h4>Get in Touch</h4>
  <div class="contact-line"><svg width="12" height="16" viewBox="0 0 12 16"><path d="M6 0a6 6 0 0 0-6 6c0 4.5 6 10 6 10s6-5.5 6-10a6 6 0 0 0-6-6zm0 8.5A2.5 2.5 0 1 1 6 3.5a2.5 2.5 0 0 1 0 5z" fill="#333"/></svg><span>406 Cooper Lane<br>Millbrook, OH 43902</span></div>
  <div class="contact-line"><svg width="13" height="13" viewBox="0 0 16 16"><path d="M3.6 1 6 3.7 4.7 5.6a9 9 0 0 0 5.7 5.7L12.3 10 15 12.4l-1.4 2.4C7.5 15 1 8.5 1.2 2.4z" fill="#333"/></svg><b>555-014-2270</b></div>
  <div class="contact-line"><svg width="15" height="12" viewBox="0 0 15 12"><rect x="1" y="1" width="13" height="10" fill="none" stroke="#333" stroke-width="1.5"/><path d="M1 1l6.5 5L14 1" fill="none" stroke="#333" stroke-width="1.5"/></svg><u>info@ridgewayfw.com</u></div>
</div>

<footer class="site-footer">
  <div class="footer-brand"><div class="brand-dot"></div><span>Ridgeway Fluidworks</span></div>
  <nav class="footer-nav"><a class="active">Home</a><a>About Us</a><a>Our Services</a><a>Testimonials</a><a>FAQs</a><a>Terms of Use</a><a>Contact Us</a></nav>
  <div class="social"><i class="on"></i><i></i><i></i></div>
  <div class="footer-rule"></div>
  <div class="copyright">© 2018 by Ridgeway Fluidworks. All rights reserved.</div>
  <div class="legal"><a>Site Mape</a><a>Disclaimer</a><a>Privacy Policy</a></div>
</footer>

</body>
</html>
```